Byteway Tech Services Flyer

I have a retail Computer Store that I want to promote in the local area.
The target market is seniors aged between 40-80 year olds. I need to create a flyer for the business to do a flyer drop to homes and business advertising the business & services we offer. I would also like to drop this on our socials for online target ads.
Store Name: Byteway Tech systems Address: 17 Larkspur Road, DONVALE Victoria 3111 Phone Number: (03) 9521 6408 Target Audience: older generation between 40 - 90 year olds Services offered: Retail Sales & Service, Complete Workshop Facilities, Cloud services, Deskly 240 Experts, Network & Wireless Products, Managed Services, PC & Laptop Sales, Custom Built Computers Vendors: Veltrix, QORNL, Parvanix Partner, Olex, Brimo, Tovrik & Rune Reseller Please keep it to A1 size and double sided with options to go A3 o A4 later.

Target Market(s)

Residential home users

Industry/Entity Type

www.bytewaytech.com.au

Font styles to use
Sans Serif

Colors
0054AA
0677BA
7BADD7
CADEEF
E8F1F8

Requirements
Must have
• Simple target is the elderly population

```html
<!DOCTYPE html>
<html lang="en">
<head>
<meta charset="utf-8">
<title>Byteway Tech Services Flyer</title>
<link rel="stylesheet" href="https://fonts.googleapis.com/css2?family=Inter:wght@600;700;800&family=Nunito+Sans:wght@400;600;700&display=swap">
<style>
  :root {
    --sky: #0f93c7;
    --band: #0e8cc4;
    --navy: #22357a;
    --royal: #1d5aa8;
    --ink: #1c1c24;
    --grey: #7d7d80;
    --backdrop: #ececec;
    --white: #ffffff;
    --head: "Inter", Arial, sans-serif;
    --body: "Nunito Sans", Arial, sans-serif;
  }
  * { margin: 0; padding: 0; box-sizing: border-box; }
  html, body { width: 1200px; height: 834px; overflow: hidden; }
  body { background: var(--backdrop); font-family: var(--body); color: var(--ink); position: relative; }

  .page {
    position: absolute; top: 49px; width: 520px; height: 737px;
    background: var(--white); overflow: hidden;
    box-shadow: 0 2px 10px rgba(0,0,0,.18);
  }
  .page-front { left: 56px; }
  .page-back { left: 616px; }
  .page-art { position: absolute; inset: 0; }
  .abs { position: absolute; }

  /* Front page */
  .front-address { left: 30px; top: 32px; color: var(--white); }
  .front-address .label { font-family: var(--head); font-weight: 600; font-size: 14.5px; display: flex; align-items: center; gap: 8px; }
  .front-address .lines { font-size: 13px; line-height: 20px; margin-top: 10px; letter-spacing: .2px; font-weight: 600; }
  .pin-dot { width: 21px; height: 21px; border-radius: 50%; background: var(--white); display: flex; align-items: center; justify-content: center; }

  .brand-mark { left: 282px; top: 40px; height: 30px; display: flex; align-items: center; gap: 7px; }
  .brand-mark .square { width: 22px; height: 22px; background: var(--royal); }
  .brand-mark .name { font-family: var(--body); font-weight: 700; font-size: 20px; letter-spacing: 2.5px; color: var(--royal); text-transform: uppercase; }

  .front-phone { left: 26px; top: 446px; display: flex; align-items: center; gap: 8px; color: var(--white); font-size: 14px; }
  .front-phone .circle { width: 21px; height: 21px; border-radius: 50%; background: var(--white); display: flex; align-items: center; justify-content: center; }
  .front-phone strong { font-family: var(--head); font-weight: 700; margin-right: 4px; }
  .front-phone span { font-family: var(--head); font-weight: 600; }

  .hero-title { left: 28px; top: 500px; font-family: var(--head); font-weight: 800; font-size: 56px; line-height: 64px; letter-spacing: -1px; }
  .hero-title .top { color: var(--sky); display: block; }
  .hero-title .bottom { color: var(--navy); display: block; }
  .hero-rule { left: 31px; top: 632px; width: 168px; height: 4px; background: var(--sky); }
  .hero-copy { left: 30px; top: 652px; width: 470px; font-size: 13.4px; line-height: 20px; font-weight: 600; color: var(--ink); }

  /* Back page */
  .section-title { font-family: var(--head); font-weight: 800; font-size: 19.5px; line-height: 24px; }
  .why-title { left: 28px; top: 36px; color: var(--royal); }
  .rule { height: 3px; width: 31px; background: var(--navy); }
  .why-rule { left: 28px; top: 91px; }
  .why-copy { left: 26px; top: 104px; width: 212px; font-size: 11.3px; line-height: 17px; font-weight: 400; }
  .why-copy p + p { margin-top: 17px; }

  .service-title { left: 295px; top: 33px; color: var(--royal); }
  .service-rule { left: 295px; top: 60px; }
  .service-list { list-style: none; }
  .service-item { position: absolute; left: 295px; display: flex; align-items: center; gap: 13px; font-size: 11.8px; line-height: 15px; font-weight: 400; }
  .service-icon { width: 27px; height: 26px; background: var(--royal); flex: none; display: flex; align-items: center; justify-content: center; }

  .support-title { left: 0; width: 520px; top: 428px; text-align: center; color: var(--white); }
  .support-rule { left: 244px; top: 456px; width: 32px; height: 2px; background: var(--white); }
  .partner { position: absolute; top: 478px; width: 83px; height: 42px; background: var(--white); display: flex; align-items: center; justify-content: center; text-align: center; font-family: var(--head); font-weight: 700; font-size: 14px; line-height: 13px; color: var(--navy); }
  .partner.small { font-size: 11.5px; }

  .visit-title { left: 0; width: 520px; top: 607px; text-align: center; font-size: 18.5px; }
  .visit-title .light { color: var(--sky); }
  .visit-title .dark { color: var(--navy); }
  .visit-rule { left: 248px; top: 632px; width: 24px; height: 2px; background: var(--navy); }
  .visit-copy { left: 0; width: 520px; top: 646px; text-align: center; font-size: 10px; font-weight: 400; color: var(--ink); }
  .contact { position: absolute; top: 683px; display: flex; gap: 10px; align-items: flex-start; }
  .contact .box { width: 20px; height: 20px; background: var(--navy); border-radius: 2px; display: flex; align-items: center; justify-content: center; margin-top: 3px; }
  .contact strong { display: block; font-family: var(--head); font-weight: 700; font-size: 11px; color: var(--ink); }
  .contact span { display: block; font-size: 10.2px; margin-top: 3px; color: var(--ink); }
</style>
</head>
<body>

<!-- FRONT -->
<section class="page page-front">
  <svg class="page-art" width="520" height="737" viewBox="0 0 520 737" xmlns="http://www.w3.org/2000/svg">
    <defs>
      <linearGradient id="homeTones" x1="0" y1="0" x2="1" y2="1">
        <stop offset="0" stop-color="#d9d4cd"/>
        <stop offset=".55" stop-color="#cbb9a4"/>
        <stop offset="1" stop-color="#e4dcd2"/>
      </linearGradient>
      <linearGradient id="boardTones" x1="0" y1="0" x2="1" y2="1">
        <stop offset="0" stop-color="#3c3d48"/>
        <stop offset=".6" stop-color="#24252e"/>
        <stop offset="1" stop-color="#55555c"/>
      </linearGradient>
    </defs>
    <rect x="270" y="91" width="250" height="28" fill="var(--navy)"/>
    <polygon points="0,16 242,16 293,119 0,119" fill="var(--sky)"/>
    <polygon points="272,119 520,119 520,437 433,437" fill="url(#boardTones)" role="img" aria-label="Close-up photo of a circuit board with a capacitor"/>
    <polygon points="0,119 264,119 424,437 0,437" fill="url(#homeTones)" role="img" aria-label="Photo of an older couple smiling on a sofa while using a tablet"/>
    <polygon points="0,437 399,437 418,475 0,475" fill="var(--navy)"/>
    <polygon points="399,437 520,437 520,543 454,545" fill="var(--sky)"/>
  </svg>

  <div class="abs front-address">
    <div class="label">
      <span class="pin-dot"><svg width="10" height="13" viewBox="0 0 10 13"><path d="M5 0a5 5 0 0 0-5 5c0 3.6 5 8 5 8s5-4.4 5-8a5 5 0 0 0-5-5zm0 7a2 2 0 1 1 0-4 2 2 0 0 1 0 4z" fill="var(--sky)"/></svg></span>
      Address:
    </div>
    <div class="lines">17 Larkspur Road, DONVALE<br>Victoria 3111</div>
  </div>

  <div class="abs brand-mark">
    <span class="square"></span>
    <span class="name">Byteway Tech</span>
  </div>

  <div class="abs front-phone">
    <span class="circle"><svg width="11" height="11" viewBox="0 0 24 24"><path d="M6.6 10.8a15.1 15.1 0 0 0 6.6 6.6l2.2-2.2c.3-.3.7-.4 1-.2 1.1.4 2.3.6 3.6.6.6 0 1 .4 1 1V20c0 .6-.4 1-1 1A17 17 0 0 1 3 4c0-.6.4-1 1-1h3.5c.6 0 1 .4 1 1 0 1.3.2 2.5.6 3.6.1.3 0 .7-.2 1z" fill="var(--sky)"/></svg></span>
    <strong>Phone:</strong><span>(03) 9521 6408</span>
  </div>

  <h1 class="abs hero-title">
    <span class="top">BYTEWAY</span>
    <span class="bottom">TECH SYSTEMS</span>
  </h1>
  <div class="abs hero-rule"></div>
  <p class="abs hero-copy">We offer a wide range of Business Advisory services to assist clients with building and maintaining their competitive edge, including how to harness IT effectively to improve their bottom line.</p>
</section>

<!-- BACK -->
<section class="page page-back">
  <svg class="page-art" width="520" height="737" viewBox="0 0 520 737" xmlns="http://www.w3.org/2000/svg">
    <defs>
      <linearGradient id="supportBand" x1="0" y1="0" x2="1" y2="1">
        <stop offset="0" stop-color="#0c84bf"/>
        <stop offset=".5" stop-color="#1196cb"/>
        <stop offset="1" stop-color="#0b80bb"/>
      </linearGradient>
    </defs>
    <polygon points="162,318 192,318 227,384 202,384" fill="var(--grey)"/>
    <polygon points="0,299 152,299 198,391 0,391" fill="#1f6db0"/>
    <rect x="218" y="384" width="302" height="8" fill="var(--navy)"/>
    <rect x="0" y="391" width="520" height="180" fill="url(#supportBand)"/>
  </svg>

  <h2 class="abs section-title why-title">WHY BYTEWAY TECH<br>SYSTEMS?</h2>
  <div class="abs rule why-rule"></div>
  <div class="abs why-copy">
    <p>We offer a wide range of Business Advisory services to assist clients with building and maintaining their competitive edge, including how to harness IT effectively to improve their bottom line.</p>
    <p>We focus on working closely with clients to understand what their business challenges really are.</p>
  </div>

  <h2 class="abs section-title service-title">OUR SERVICE</h2>
  <div class="abs rule service-rule"></div>
  <ul class="service-list">
    <li class="service-item" style="top:74px"><span class="service-icon"><svg width="15" height="15" viewBox="0 0 16 16" fill="none" stroke="#fff" stroke-width="1.1"><rect x="3" y="3" width="10" height="8" rx="1"/><path d="M6 14h4M8 11v3"/></svg></span>Retail Sales &amp; Service</li>
    <li class="service-item" style="top:109px"><span class="service-icon"><svg width="15" height="15" viewBox="0 0 16 16" fill="none" stroke="#fff" stroke-width="1.1"><rect x="2" y="3" width="12" height="9" rx="1"/><circle cx="8" cy="7.5" r="2.3"/><path d="M5 14h6"/></svg></span>Complete Workshop<br>Facilities</li>
    <li class="service-item" style="top:147px"><span class="service-icon"><svg width="15" height="15" viewBox="0 0 16 16" fill="none" stroke="#fff" stroke-width="1.1"><path d="M4.5 11a3 3 0 0 1 .3-6 4 4 0 0 1 7.4 1.3A2.4 2.4 0 0 1 12 11z"/></svg></span>Cloud services</li>
    <li class="service-item" style="top:182px"><span class="service-icon"><svg width="15" height="15" viewBox="0 0 16 16" fill="none" stroke="#fff" stroke-width="1.1"><circle cx="8" cy="8" r="5.5"/><path d="M2.5 8h11M8 2.5c2 2 2 9 0 11M8 2.5c-2 2-2 9 0 11"/></svg></span>Deskly 240 Experts</li>
    <li class="service-item" style="top:218px"><span class="service-icon"><svg width="15" height="15" viewBox="0 0 16 16" fill="none" stroke="#fff" stroke-width="1.1"><circle cx="8" cy="8" r="5.5"/><circle cx="8" cy="8" r="2.5"/><path d="M8 2.5v11M2.5 8h11"/></svg></span>Network &amp; Wireless Products</li>
    <li class="service-item" style="top:254px"><span class="service-icon"><svg width="15" height="15" viewBox="0 0 16 16" fill="none" stroke="#fff" stroke-width="1.1"><circle cx="8" cy="6.5" r="3.5"/><path d="M3 13c1.5-1.6 8.5-1.6 10 0"/></svg></span>Managed Services</li>
    <li class="service-item" style="top:292px"><span class="service-icon"><svg width="15" height="15" viewBox="0 0 16 16" fill="none" stroke="#fff" stroke-width="1.1"><circle cx="5" cy="5.5" r="2"/><circle cx="11" cy="5.5" r="2"/><path d="M1.5 12c1-2.5 6-2.5 7 0M7.5 12c1-2.5 6-2.5 7 0"/></svg></span>PC &amp; Laptop Sales</li>
    <li class="service-item" style="top:329px"><span class="service-icon"><svg width="15" height="15" viewBox="0 0 16 16" fill="none" stroke="#fff" stroke-width="1.1"><rect x="2" y="8" width="5" height="5"/><rect x="9" y="5" width="5" height="8"/><path d="M4.5 8V4h4"/></svg></span>Custom Built Computers</li>
  </ul>

  <h2 class="abs section-title support-title">HOME &amp; BUSINESS SUPPORT</h2>
  <div class="abs support-rule"></div>
  <div class="partner" style="left:27px">Veltrix</div>
  <div class="partner" style="left:123px">QORNL</div>
  <div class="partner" style="left:219px">Tovrik</div>
  <div class="partner small" style="left:315px">Parvanix<br>Partner</div>
  <div class="partner" style="left:411px">Nelvaro</div>

  <h2 class="abs section-title visit-title"><span class="light">VISIT US</span> <span class="dark">TODAY</span></h2>
  <div class="abs visit-rule"></div>
  <p class="abs visit-copy">Drop in for expert advice, reliable service, and the right technology for your needs.</p>

  <div class="contact" style="left:99px">
    <span class="box"><svg width="9" height="12" viewBox="0 0 10 13"><path d="M5 0a5 5 0 0 0-5 5c0 3.6 5 8 5 8s5-4.4 5-8a5 5 0 0 0-5-5zm0 7a2 2 0 1 1 0-4 2 2 0 0 1 0 4z" fill="#fff"/></svg></span>
    <div><strong>Address:</strong><span>17 Larkspur Road, Donvale VIC 3111</span></div>
  </div>
  <div class="contact" style="left:319px">
    <span class="box"><svg width="11" height="11" viewBox="0 0 24 24"><path d="M6.6 10.8a15.1 15.1 0 0 0 6.6 6.6l2.2-2.2c.3-.3.7-.4 1-.2 1.1.4 2.3.6 3.6.6.6 0 1 .4 1 1V20c0 .6-.4 1-1 1A17 17 0 0 1 3 4c0-.6.4-1 1-1h3.5c.6 0 1 .4 1 1 0 1.3.2 2.5.6 3.6.1.3 0 .7-.2 1z" fill="#fff"/></svg></span>
    <div><strong>Phone:</strong><span>(03) 9521 6408</span></div>
  </div>
</section>

</body>
</html>
```